Waterless soap seeking funky new design

We are looking for a talented designer to create a fresh and appealing label design for one of our current products. We do have a current logo that we really like and use in several places. We would like the new label design to work with and incorporate the current logo.
The product is our Gravel Tide wipe-off soap. It is made by hand, in small batches. We would like the label design to reflect the hand made aspect of the product. We are not requiring the label to be illustrated but we do like the hand drawn and hand made tie. and the illustration does appeal to us.
Please see the attached current logo that we do like. you can see it used in the attached current label, that we DONT like. this is what we are seeking, a new label for our Gravel Tide soap.
The soap is made for real messes, grease, grime and busted knuckles. It is made using natural ingredients. this is not a Men Only product, it is definitely geared toward men and would like the label to reflect that.

Target Market(s)

Mechanics, tradesmen, welders, People who get dirty for a living

Colors
0054AA
0677BA
7BADD7
CADEEF
E8F1F8
EE7325
F08F49
F5BC92
FAE3D3
FDF4ED
EB3D1F
EC4F4E
F09395
F8D3D4
FCEDEE

Requirements
Must have
• Keep the current logo. It can play a smaller role in the label, but we do use this logo else were in other promo items, and we don't want it to be completely gone.
Nice to have
• I would like to have something illustrated, I am not sold on this but I like the idea of a hand drawn(or at least in part) label to tie into the 'hand made' aspect
Should not have
• Current Font styles, We are currently selling product but we don't care for our font styles.

```html
<!DOCTYPE html>
<html lang="en">
<head>
<meta charset="utf-8">
<title>Gravel Tide Wipe-Off Soap – Label Set</title>
<link href="https://fonts.googleapis.com/css2?family=Anton&family=Oswald:wght@500;600&family=Pathway+Gothic+One&display=swap" rel="stylesheet">
<style>
  :root {
    --label-yellow: #f8ad06;
    --band-navy: #0d3b6c;
    --band-black: #0b0b0b;
    --ink-navy: #14335c;
    --logo-orange: #f5ae2a;
    --white: #ffffff;
    --page: #ffffff;
  }
  * { box-sizing: border-box; margin: 0; padding: 0; }
  html, body { width: 780px; height: 1200px; overflow: hidden; background: var(--page); }
  .canvas { position: relative; width: 780px; height: 1200px; }

  .label {
    position: absolute; left: 50px; width: 680px; height: 575px;
    background: var(--label-yellow); overflow: hidden;
  }
  .label--navy { top: 12px; --band: var(--band-navy); --badge-text: var(--white); }
  .label--black { top: 613px; --band: var(--band-black); --badge-text: var(--label-yellow); }

  .torn-band { position: absolute; inset: 0; width: 680px; height: 575px; }
  .torn-band path { fill: var(--band); }

  .tagline {
    position: absolute; left: 40px; width: 300px; top: 24px; text-align: center;
    font-family: "Oswald", sans-serif; font-weight: 600; font-size: 11.5px;
    line-height: 15px; color: var(--ink-navy); text-transform: uppercase; letter-spacing: 0.2px;
  }

  .brand-mark {
    position: absolute; left: 73px; top: 92px; width: 234px; height: 234px;
    border-radius: 50%; background: var(--logo-orange);
    display: flex; flex-direction: column; align-items: center; justify-content: center;
    font-family: "Oswald", sans-serif; font-weight: 600; color: var(--ink-navy);
    text-transform: uppercase; text-align: center; letter-spacing: 2px; font-size: 28px; line-height: 34px;
  }

  .product-title {
    position: absolute; left: 20px; width: 340px; top: 332px; text-align: center;
    font-family: "Anton", sans-serif; color: var(--white); text-transform: uppercase;
    font-size: 52px; line-height: 60px; letter-spacing: -0.5px;
  }

  .badges { position: absolute; left: 52px; top: 452px; width: 290px; display: flex; justify-content: space-between; }
  .badge { display: flex; align-items: center; gap: 8px; }
  .badge svg { width: 36px; height: 36px; flex: none; }
  .badge__text {
    font-family: "Oswald", sans-serif; font-weight: 600; font-size: 13px; line-height: 17px;
    color: var(--badge-text);
  }

  .net-weight {
    position: absolute; left: 115px; top: 520px;
    font-family: "Oswald", sans-serif; font-weight: 600; font-size: 20px; color: var(--ink-navy);
  }
  .origin { position: absolute; left: 195px; top: 522px; display: flex; align-items: center; gap: 6px; }
  .origin svg { width: 36px; height: 26px; }
  .origin__text {
    font-family: "Oswald", sans-serif; font-weight: 600; font-size: 11px; line-height: 12px;
    color: var(--ink-navy); text-transform: uppercase;
  }

  .info { position: absolute; left: 419px; top: 20px; width: 245px; }
  .info__intro {
    font-family: "Oswald", sans-serif; font-weight: 500; font-size: 14px; line-height: 17px;
    color: var(--ink-navy); margin-bottom: 9px;
  }
  .info__block { font-family: "Pathway Gothic One", sans-serif; color: var(--white); font-size: 11.4px; line-height: 14.3px; margin-bottom: 5px; }
  .info__heading { font-family: "Oswald", sans-serif; font-weight: 600; font-size: 12.5px; line-height: 14px; }

  .footer { position: absolute; left: 419px; top: 518px; width: 245px; }
  .footer__made, .footer__site {
    font-family: "Oswald", sans-serif; font-weight: 500; font-size: 13px; line-height: 21px; color: var(--ink-navy);
  }
  .footer__lot {
    position: absolute; left: 166px; top: 2px; font-family: "Oswald", sans-serif; font-weight: 500;
    font-size: 6.5px; line-height: 8px; color: var(--ink-navy);
  }
  .footer__lot span { display: block; }
  .footer__lot .lot-line { margin-bottom: 8px; }
</style>
</head>
<body>
<svg width="0" height="0" style="position:absolute" aria-hidden="true">
  <defs>
    <symbol id="torn-band-shape" viewBox="0 0 680 575">
      <path d="M0,80 L14,70 22,78 34,62 44,74 58,66 66,78 80,68 92,76 104,60 114,72 128,66 138,80 152,68 164,74 176,58 186,72 200,66 212,78 226,64 236,74 250,68 262,80 276,62 288,72 300,66 312,78 326,68 338,74 350,60 362,72 376,66 388,80 402,68 414,74 428,58 440,72 454,66 466,78 480,64 492,74 506,68 518,80 532,62 544,72 558,66 570,78 584,68 596,74 610,60 622,72 636,66 648,80 662,68 680,74 L680,508 668,516 656,504 644,520 632,506 620,514 606,500 594,512 580,506 568,520 556,504 544,514 530,508 518,518 504,502 492,512 478,506 466,520 452,504 440,514 428,500 416,512 402,506 390,520 376,504 364,514 350,508 338,518 324,502 312,512 298,506 286,520 272,504 260,514 248,500 236,512 222,506 210,520 196,504 184,514 170,508 158,518 144,502 132,512 118,506 106,520 92,504 80,514 68,500 56,512 42,506 30,520 16,504 0,512 Z"/>
    </symbol>
    <symbol id="icon-hand" viewBox="0 0 36 36">
      <path d="M9,30 C6,26 5,20 6,17 L8,17 L10,22 L10,8 C10,6 13,6 13,8 L13,17 L14,5 C14,3 17,3 17,5 L17,17 L18,6 C18,4 21,4 21,6 L21,17 L22,9 C22,7 25,7 25,9 L25,22 C25,27 22,31 18,31 L12,31 Z" fill="#fff"/>
      <path d="M4,6 L5,9 8,10 5,11 4,14 3,11 0,10 3,9 Z M31,24 L32,26 34,27 32,28 31,30 30,28 28,27 30,26 Z" fill="#fff"/>
    </symbol>
    <symbol id="icon-no-water" viewBox="0 0 36 36">
      <circle cx="18" cy="18" r="15" fill="none" stroke="#fff" stroke-width="2.5"/>
      <path d="M18,8 C14,14 12,17 12,20 C12,24 15,26 18,26 C21,26 24,24 24,20 C24,17 22,14 18,8 Z" fill="#fff"/>
      <line x1="8" y1="28" x2="28" y2="8" stroke="currentColor" stroke-width="3"/>
    </symbol>
    <symbol id="icon-flag" viewBox="0 0 36 26">
      <rect width="36" height="26" fill="#fff"/>
      <g fill="#c8202f">
        <rect y="0" width="36" height="2"/><rect y="4" width="36" height="2"/><rect y="8" width="36" height="2"/>
        <rect y="12" width="36" height="2"/><rect y="16" width="36" height="2"/><rect y="20" width="36" height="2"/><rect y="24" width="36" height="2"/>
      </g>
      <rect width="15" height="14" fill="#1c3a78"/>
    </symbol>
  </defs>
</svg>

<main class="canvas">
  <!-- Navy edition -->
  <section class="label label--navy">
    <svg class="torn-band" viewBox="0 0 680 575" aria-hidden="true"><use href="#torn-band-shape"/></svg>
    <p class="tagline">Rinse-free cleanser for hands that work<br>Tough on grime. Gentle on skin</p>
    <div class="brand-mark"><span>Bristle Works</span><span>Soap Co.</span></div>
    <h1 class="product-title">Gravel Tide<br>Wipe-Off Soap</h1>
    <div class="badges">
      <div class="badge"><svg aria-hidden="true"><use href="#icon-hand"/></svg><span class="badge__text">Eczema<br>Friendly</span></div>
      <div class="badge" style="color:var(--band)"><svg aria-hidden="true"><use href="#icon-no-water"/></svg><span class="badge__text">No Water?<br>No Problem.</span></div>
    </div>
    <p class="net-weight">12 oz</p>
    <div class="origin"><svg aria-hidden="true"><use href="#icon-flag"/></svg><span class="origin__text">Made<br>in USA</span></div>
    <div class="info">
      <p class="info__intro">Handmade in small batches,<br>All-Natural, No fillers</p>
      <div class="info__block"><p class="info__heading">Description:</p>Bristle Works Gravel Tide is tough where it counts. Built for busted knuckles and real dirt. This no-rinse soap is built to cut grease, grime, and grit without burning cracked hands. With bentonite clay, panthenol, vitamin E and D-Limonene, it powers through the mess – then wipes off clean. Made for mechanics, field workers, and hard-working hands. No water needed. Power clean your hands wherever the job takes you. No rinse. No sting. Just clean</div>
      <div class="info__block"><p class="info__heading">Directions:</p>Apply to dry skin. Rub gently to lift dirt and oils. Wipe clean with towel or cloth. Rinsing is optional- effective with or with out water</div>
      <div class="info__block">For external use only. Patch test recommended. Discontinue if irritation occurs. See full info at bristleworkssoap.com</div>
      <div class="info__block"><p class="info__heading">Ingredients:</p>Water (Aqua), Glycerin, Cocamidopropyl Betaine, Decyl Glucoside, Lauryl Glucoside, Tremella Fuciformis (Mushroom) Extract, Avena Sativa (Oat) Kernel Flour, Helianthus Annuus (Sunflower) Seed Oil, Cetearyl Alcohol, Emulsifying Wax NF, Bentonite, Panthenol (Provitamin B5), Tocopherol (Vitamin E), D-Limonene*, Citric Acid, Presero Blend (Propylene Glycol, Diazolidinyl Urea, Iodopropynyl Butylcarbamate). *From natural citrus peel oils</div>
    </div>
    <div class="footer">
      <p class="footer__made">Made In SLC, UT</p>
      <p class="footer__site">bristleworkssoap.com</p>
      <p class="footer__lot"><span class="lot-line">Lot#</span><span>Best if used within</span><span>24 Months of opening</span></p>
    </div>
  </section>

  <!-- Black edition -->
  <section class="label label--black">
    <svg class="torn-band" viewBox="0 0 680 575" aria-hidden="true"><use href="#torn-band-shape"/></svg>
    <p class="tagline">Rinse-free cleanser for hands that work<br>Tough on grime. Gentle on skin</p>
    <div class="brand-mark"><span>Bristle Works</span><span>Soap Co.</span></div>
    <h1 class="product-title">Gravel Tide<br>Wipe-Off Soap</h1>
    <div class="badges">
      <div class="badge"><svg aria-hidden="true"><use href="#icon-hand"/></svg><span class="badge__text">Eczema<br>Friendly</span></div>
      <div class="badge" style="color:var(--band)"><svg aria-hidden="true"><use href="#icon-no-water"/></svg><span class="badge__text">No Water?<br>No Problem.</span></div>
    </div>
    <p class="net-weight">12 oz</p>
    <div class="origin"><svg aria-hidden="true"><use href="#icon-flag"/></svg><span class="origin__text">Made<br>in USA</span></div>
    <div class="info">
      <p class="info__intro">Handmade in small batches,<br>All-Natural, No fillers</p>
      <div class="info__block"><p class="info__heading">Description:</p>Bristle Works Gravel Tide is tough where it counts. Built for busted knuckles and real dirt. This no-rinse soap is built to cut grease, grime, and grit without burning cracked hands. With bentonite clay, panthenol, vitamin E and D-Limonene, it powers through the mess – then wipes off clean. Made for mechanics, field workers, and hard-working hands. No water needed. Power clean your hands wherever the job takes you. No rinse. No sting. Just clean</div>
      <div class="info__block"><p class="info__heading">Directions:</p>Apply to dry skin. Rub gently to lift dirt and oils. Wipe clean with towel or cloth. Rinsing is optional- effective with or with out water</div>
      <div class="info__block">For external use only. Patch test recommended. Discontinue if irritation occurs. See full info at bristleworkssoap.com</div>
      <div class="info__block"><p class="info__heading">Ingredients:</p>Water (Aqua), Glycerin, Cocamidopropyl Betaine, Decyl Glucoside, Lauryl Glucoside, Tremella Fuciformis (Mushroom) Extract, Avena Sativa (Oat) Kernel Flour, Helianthus Annuus (Sunflower) Seed Oil, Cetearyl Alcohol, Emulsifying Wax NF, Bentonite, Panthenol (Provitamin B5), Tocopherol (Vitamin E), D-Limonene*, Citric Acid, Presero Blend (Propylene Glycol, Diazolidinyl Urea, Iodopropynyl Butylcarbamate). *From natural citrus peel oils</div>
    </div>
    <div class="footer">
      <p class="footer__made">Made In SLC, UT</p>
      <p class="footer__site">bristleworkssoap.com</p>
      <p class="footer__lot"><span class="lot-line">Lot#</span><span>Best if used within</span><span>24 Months of opening</span></p>
    </div>
  </section>
</main>
</body>
</html>
```